Holiday Rental Company Flyer Design (DL not A5)

Note from PixelFolk Administration: The category sizing selected is A5, however the project requires DL sized artwork. Please refer to the DL template link below while the 'Special Requirements' are updated accordingly.

Project Brief:
We need a double sided DL flyer designed for an up market Holiday Rental Company that portrays a personalised approach to property management. These are to be used for letter box drops to homes we're specifically targeting so the design should be modern, complimentary colour palette, uncluttered & visually appealing.

Please Download the DL Template from Quillmark here: http://www.quillmark.com.au/qm/ns/propath/UploadResources.aspx?selectedTab=0?pfid=BFB&pf_id=BFB&xnav=easypath-upload-image#Templates

Target Market(s)

Wealthy Home Owners

Industry/Entity Type

It Company

Font styles to use
Other font styles liked:
• Avant Garde Extra Light & Demi

Colors
33b8a4

Requirements
Must have
• DL Flyer sizes (210mm width x 99mm width, plus 3mm bleed)
• Front: Logo, Main Image & Grab
• Back: Contact Details & Brief Description of our business
• Images: Ideally the main image should be the house with the pool but alternatively a lifestyle images could also be used.
Nice to have
• A creative designer!
Should not have
• Clutter & busy designs

```html
<!DOCTYPE html>
<html lang="en">
<head>
<meta charset="utf-8">
<title>Harbourline Stays – DL Flyer</title>
<link rel="stylesheet" href="https://fonts.googleapis.com/css2?family=Montserrat:wght@200&family=Inter+Tight:wght@300&display=swap">
<style>
  :root {
    --teal-deep: #27b38f;
    --teal-bright: #4fdbc2;
    --teal-pale: #7fe3d1;
    --ink: #1f2424;
    --paper: #ffffff;
    --stage: #000000;
    --photo-dusk-a: #4b4a86;
    --photo-dusk-b: #6f6cb8;
    --photo-stone-a: #a39a8f;
    --photo-stone-b: #b9784f;
    --photo-linen-a: #e4d4b6;
    --photo-linen-b: #d6c66a;
    --display: "Montserrat", sans-serif;
    --body: "Inter Tight", sans-serif;
  }
  * { box-sizing: border-box; margin: 0; padding: 0; }
  html, body { width: 1200px; height: 1000px; overflow: hidden; background: var(--stage); }
  .canvas { position: relative; width: 1200px; height: 1000px; }

  .flyer { position: absolute; top: 74px; width: 414px; height: 851px; overflow: hidden; }
  .flyer--front { left: 122px; background: var(--teal-deep); }
  .flyer--back { left: 665px; background: var(--paper); }
  .shapes { position: absolute; inset: 0; width: 100%; height: 100%; }

  .brand { position: absolute; left: 0; width: 100%; text-align: center; font-family: var(--display); font-weight: 200; text-transform: uppercase; }
  .brand--front { top: 86px; color: var(--paper); font-size: 37px; line-height: 44px; letter-spacing: 3px; }
  .brand--back { top: 62px; left: 190px; width: 212px; color: var(--teal-deep); font-size: 18px; line-height: 21px; letter-spacing: 1.5px; }
  .brand-dot { display: block; margin: 14px auto 0; border: 1px solid currentColor; border-radius: 50%; }
  .brand--front .brand-dot { width: 58px; height: 58px; }
  .brand--back .brand-dot { width: 26px; height: 26px; margin-top: 10px; }

  .photo { position: absolute; }
  .photo--pool { left: 0; top: 314px; width: 414px; height: 255px;
    background: linear-gradient(135deg, var(--photo-dusk-a), var(--photo-dusk-b)); }
  .photo--vase { left: 0; top: 186px; width: 201px; height: 128px;
    background: linear-gradient(90deg, var(--photo-stone-a), var(--photo-stone-b)); }
  .photo--bed { left: 213px; top: 186px; width: 201px; height: 128px;
    background: linear-gradient(135deg, var(--photo-linen-a), var(--photo-linen-b)); }

  .tagline { position: absolute; left: 135px; top: 693px; width: 270px; transform: rotate(-45deg); transform-origin: center;
    font-family: var(--body); font-weight: 300; font-size: 17px; line-height: 20px; color: var(--ink); text-align: center; }

  .copy { position: absolute; left: 48px; top: 360px; width: 318px; font-family: var(--body); font-weight: 300;
    font-size: 13px; line-height: 17px; color: var(--ink); letter-spacing: -0.15px; }
  .copy p { margin-bottom: 17px; text-align: justify; }
  .copy .lead { text-align: left; }
  .benefits { list-style: none; }
  .benefits li { position: relative; padding-left: 40px; margin-bottom: 17px; text-align: justify; }
  .benefits li::before { content: ""; position: absolute; left: 2px; top: 3px; width: 26px; height: 26px;
    border: 1px solid var(--teal-bright); border-radius: 50%; }
  .contact span { display: block; }
</style>
</head>
<body>
<div class="canvas">

  <section class="flyer flyer--front">
    <svg class="shapes" viewBox="0 0 414 851" preserveAspectRatio="none" aria-hidden="true">
      <polygon points="0,206 0,314 106,314" fill="var(--teal-bright)"/>
      <polygon points="0,569 358,569 78,851 0,851" fill="var(--teal-bright)"/>
      <polygon points="0,575 0,606 200,790 218,770" fill="var(--teal-pale)"/>
      <polygon points="258,569 358,569 308,619" fill="var(--teal-pale)"/>
    </svg>
    <h1 class="brand brand--front">Harbourline<br>Stays<span class="brand-dot"></span></h1>
    <div class="photo photo--pool" role="img" aria-label="Photograph: modern home with a lit swimming pool at dusk"></div>
    <p class="tagline">Holiday Rental Management<br>with a difference</p>
  </section>

  <section class="flyer flyer--back">
    <svg class="shapes" viewBox="0 0 414 851" preserveAspectRatio="none" aria-hidden="true">
      <polygon points="0,0 60,0 126,70 20,174 0,174" fill="var(--teal-deep)"/>
      <polygon points="126,70 140,84 48,174 22,174" fill="var(--teal-pale)"/>
      <polygon points="140,84 232,174 48,174" fill="var(--teal-bright)"/>
      <polygon points="0,326 175,326 0,502" fill="var(--teal-pale)"/>
      <polygon points="0,326 90,326 0,416" fill="var(--teal-bright)"/>
      <polygon points="414,702 352,763 414,763" fill="var(--teal-pale)"/>
      <polygon points="414,763 352,763 414,823" fill="var(--teal-bright)"/>
    </svg>
    <h2 class="brand brand--back">Harbourline<br>Stays<span class="brand-dot"></span></h2>
    <div class="photo photo--vase" role="img" aria-label="Photograph: interior with orange flowers in a glass vase and candles"></div>
    <div class="photo photo--bed" role="img" aria-label="Photograph: bedroom with yellow cushions on a colourful quilt"></div>

    <div class="copy">
      <p class="lead">What we do differently!</p>
      <p>Rather than relying upon a key safe or a central pick-up destination, a ‘Harbourline Stays’ staff member will greet guests upon arrival.</p>
      <p>Our ‘Meet &amp; Greet’ service provides home owners with an increased level of Security and also allows us to:</p>
      <ul class="benefits">
        <li>Prepare the home for their arrival (lights, heaters, music etc.)</li>
        <li>Establish a rapport &amp;help facilitate future bookings</li>
        <li>Reiterate their responsibilities to ensure the return of their bond</li>
      </ul>
      <p class="lead">If you’d like to know what your property could achieve or require additional information, please contact us on:</p>
      <p class="lead contact">
        <span>t: (03)5900 1234</span>
        <span>e: stay@harbourlinestays.com.au</span>
        <span>w: harbourlinestays.com.au</span>
      </p>
      <p class="lead">PO Box 12, Larkfield Victoria 3900</p>
    </div>
  </section>

</div>
</body>
</html>
```